Flyer for Makeup Class

A flyer for my makeup class promotion. I am a make up artist starting a group class to teach makeup to ladies. I have attached some verbiage handwritten. My picture is the one in pink hijab. I have also attached some inspiration ideas and color combination (the colors in the cake design are the ones I want to use).

Target Market(s)

Ladies looking to learn make up from a make up artist

Industry/Entity Type

Hair And Beauty

Requirements
Must have
• The verbiage / description that I have hand written should be written using graphics and nice fonts. You can change the exact wording to make it better.

```html
<!DOCTYPE html>
<html lang="en">
<head>
<meta charset="utf-8">
<title>Exclusive Makeup Master Class Flyer</title>
<link rel="stylesheet" href="https://fonts.googleapis.com/css2?family=Chivo:wght@300;700&family=Open+Sans:wght@400&display=swap">
<style>
  :root {
    --page: #ffffff;
    --pink-soft: #f3d3d6;
    --pink-mid: #e8b4bb;
    --pink-deep: #e46a92;
    --blush: #f7e3e4;
    --ink: #2f3b4c;
    --band: #000000;
    --band-text: #ffffff;
    --panel: rgba(246, 205, 218, 0.55);
  }
  * { margin: 0; padding: 0; box-sizing: border-box; }
  html, body { width: 1200px; height: 1200px; overflow: hidden; background: var(--page); }
  .stage { position: relative; width: 1200px; height: 1200px; }
  .flyer {
    position: absolute; left: 200px; top: 34px;
    width: 854px; height: 1208px;
    transform: scale(0.937); transform-origin: 0 0;
    overflow: hidden;
    background:
      radial-gradient(circle at 8% 8%, rgba(228,80,130,0.55) 0, rgba(228,80,130,0) 22%),
      radial-gradient(circle at 30% 5%, rgba(236,140,180,0.5) 0, rgba(236,140,180,0) 12%),
      radial-gradient(circle at 90% 55%, rgba(255,255,255,0.6) 0, rgba(255,255,255,0) 25%),
      radial-gradient(circle at 85% 15%, rgba(255,255,255,0.55) 0, rgba(255,255,255,0) 20%),
      linear-gradient(160deg, var(--pink-mid) 0%, var(--pink-soft) 45%, var(--blush) 100%);
    color: var(--ink);
  }
  .block { position: absolute; white-space: nowrap; }
  .title {
    left: 0; width: 854px; text-align: center;
    font-family: "Chivo", sans-serif; font-weight: 300;
    font-size: 76px; line-height: 70px; letter-spacing: 1px;
    top: 78px;
  }
  .byline {
    left: 0; width: 854px; text-align: center; top: 220px;
    font-family: "Chivo", sans-serif; font-weight: 700;
  }
  .byline .by { font-size: 30px; line-height: 36px; }
  .byline .name { font-size: 32px; line-height: 40px; }
  .byline .role { font-size: 18px; line-height: 24px; }
  .portrait {
    position: absolute; left: 0; top: 330px; width: 545px; height: 649px;
    background:
      radial-gradient(ellipse at 50% 30%, #f1c9b8 0, #f4c6bf 22%, rgba(244,198,191,0) 40%),
      linear-gradient(180deg, #f6cfc6 0%, #f3c2bd 55%, #d5457f 100%);
    border-radius: 46% 46% 0 0 / 30% 30% 0 0;
  }
  .venue { left: 432px; top: 400px; font-family: "Open Sans", sans-serif; }
  .venue .label { font-size: 42px; line-height: 54px; }
  .venue .place { font-size: 25px; line-height: 31px; }
  .venue .date { font-size: 41px; line-height: 52px; margin-top: 6px; }
  .venue .time { font-size: 34px; line-height: 40px; }
  .audience {
    position: absolute; left: 474px; top: 739px; width: 347px; height: 217px;
    background: var(--panel); text-align: center;
  }
  .audience .heading {
    font-family: "Chivo", sans-serif; font-weight: 300;
    font-size: 40px; line-height: 44px; margin-top: 32px; letter-spacing: 1px;
  }
  .audience .list {
    font-family: "Chivo", sans-serif; font-weight: 300;
    font-size: 24px; line-height: 31px; margin-top: 8px;
  }
  .band {
    position: absolute; left: 0; top: 979px; width: 854px; height: 229px;
    background: var(--band); color: var(--band-text);
    font-family: "Chivo", sans-serif;
  }
  .band .summary {
    position: absolute; left: 0; top: 34px; width: 854px; text-align: center;
    font-size: 24px; line-height: 31px; font-weight: 300;
  }
  .band .book {
    position: absolute; left: 52px; top: 128px;
    font-weight: 700; font-size: 24px; line-height: 31px;
  }
  .band .phone-icon { position: absolute; left: 330px; top: 138px; width: 46px; height: 48px; }
  .band .numbers {
    position: absolute; left: 387px; top: 128px;
    font-family: "Open Sans", sans-serif; font-size: 25px; line-height: 31px;
  }
  .band .social-mark {
    position: absolute; left: 568px; top: 143px; width: 38px; height: 38px;
    background: var(--band-text); border-radius: 7px;
  }
  .band .handle {
    position: absolute; left: 618px; top: 148px;
    font-size: 20px; line-height: 26px; font-weight: 300;
  }
</style>
</head>
<body>
<div class="stage">
  <div class="flyer">
    <h1 class="block title">EXCLUSIVE MAKEUP<br>MASTER CLASS</h1>

    <div class="block byline">
      <div class="by">By</div>
      <div class="name">SAMIRA RAHMAN</div>
      <div class="role">(UK BASED MUA)</div>
    </div>

    <div class="portrait" role="img" aria-label="Portrait of the makeup artist in a pink hijab and headpiece, looking up to the right"></div>

    <div class="block venue">
      <div class="label">VENUE:</div>
      <div class="place">Lakeside Club Pavilion<br>(Hillview)</div>
      <div class="date">6yh April 2019</div>
      <div class="time">11:30 - 5:30 pm</div>
    </div>

    <div class="audience">
      <div class="heading">PERFECT FOR</div>
      <div class="list">Professionals,<br>Begginners<br>and makeup lovers</div>
    </div>

    <div class="band">
      <p class="summary">This Class is packed with loads of information tips, live demos,<br>goodie bag, certificate, Q &amp; A, Lunch and much more</p>
      <p class="book">To Book your Place<br>Contact</p>
      <svg class="phone-icon" viewBox="0 0 24 24" aria-hidden="true">
        <path fill="#ffffff" d="M6.6 2.2c.5-.3 1.1-.2 1.5.3l2.3 3.2c.3.5.3 1.1-.1 1.5L8.9 8.6c.9 2.6 3.4 5.3 6.3 6.6l1.4-1.4c.4-.4 1-.5 1.5-.2l3.3 2.1c.5.3.7 1 .4 1.5l-1.3 2.4c-.5.9-1.5 1.4-2.5 1.2C10.3 19.5 4.4 13.4 3.2 5.7c-.2-1 .3-2 1.1-2.5z"/>
      </svg>
      <p class="numbers">01700123456<br>03001234567</p>
      <span class="social-mark" aria-hidden="true"></span>
      <p class="handle">@samirarahmanmua</p>
    </div>
  </div>
</div>
</body>
</html>
```